Regenerative Medicine Brochure

I want a clean modern bi-fold or tri-fold brochure. We offer non-surgical joint repair for knees, shoulders, and hips. We have many services available including regenerative medicine including stem cell allograft, palatelet rich plasma, prolotherapy, triggerpoint injection, chiropractic and rehab therapies. We are a modern multidisciplinary clinic in coastal California. My logo is already complete and is a vibrant green color. I prefer lots of white space with some areas for service description and what conditions may benefit from the services. Design should convey modern treatments, upscale office and practice, and our target audience is older adults who want to maintain an active pain-free lifestyle.

Target Market(s)

Sports injuries, athletes, seniors who are active, knee pain, shoulder pain, arthritis.

Industry/Entity Type

Alternative Medicine

Font styles to use
Serif

Colors
9bcb3c

Requirements
Must have
• Small white space where we can write date, time, location of next event/class. Colors in brochure to coordinate with logo colors provided.

```html
<!DOCTYPE html>
<html lang="en">
<head>
<meta charset="utf-8">
<title>Coastal Vital Restore – Regenerative Medicine Brochure</title>
<link rel="stylesheet" href="https://fonts.googleapis.com/css2?family=Fjalla+One&family=Lora:wght@400;600&display=swap">
<style>
  :root{
    --green:#9bcb3c;
    --green-soft:#a9cc5e;
    --green-pale:#cfe3a4;
    --slate:#3d484c;
    --paper:#ffffff;
    --paper-grey:#ececec;
    --ink:#3b3b3b;
    --muted:#c9cdcf;
    --stage:#e6e6e6;
  }
  *{box-sizing:border-box;margin:0;padding:0}
  html,body{width:1200px;height:900px;overflow:hidden;background:var(--stage)}
  body{font-family:"Lora",Georgia,serif;color:var(--ink);position:relative}

  .spread{position:absolute;top:250px;width:585px;height:400px;display:flex;background:var(--paper);box-shadow:0 4px 14px rgba(0,0,0,.12)}
  .spread--outside{left:12px}
  .spread--inside{left:603px;background:var(--paper-grey)}
  .panel{position:relative;width:195px;height:100%;overflow:hidden}
  .spread--inside .panel{border-left:3px solid var(--paper)}
  .spread--inside .panel:first-child{border-left:none}

  .heading{font-family:"Fjalla One",Impact,sans-serif;text-transform:uppercase;color:var(--green);line-height:1.12;text-align:center;font-weight:400}
  .body-copy{font-size:7px;line-height:1.36;text-align:justify}
  .body-copy p+p{margin-top:6px}

  /* outside: expectations panel */
  .expect{padding:11px 10px}
  .expect__title{background:var(--slate);padding:10px 6px;font-size:13px;margin-bottom:9px}

  /* outside: contact panel */
  .contact{background:var(--slate)}
  .contact__top{height:124px;background:var(--green-soft);padding:10px 16px}
  .event{background:var(--paper);height:104px;padding:7px 10px}
  .event__title{font-family:"Fjalla One",Impact,sans-serif;font-size:10px;color:var(--slate);text-transform:uppercase;letter-spacing:.4px;text-align:center;margin-bottom:6px}
  .event__row{display:flex;align-items:flex-end;font-size:7px;color:var(--slate);height:19px}
  .event__label{width:38px;font-weight:600}
  .event__line{flex:1;border-bottom:1px solid var(--muted);height:1px;margin-bottom:2px}
  .contact__cta{font-size:12px;margin:10px 26px 0}
  .brand-name{font-family:"Lora",Georgia,serif;font-weight:600;color:var(--paper)}
  .contact__brand{text-align:center;margin-top:8px;font-size:15px}
  .services{margin:7px 20px 0;text-align:center;color:var(--paper)}
  .services__title{font-family:"Fjalla One",Impact,sans-serif;font-size:8.5px;color:var(--green);text-transform:uppercase;letter-spacing:.4px;margin-bottom:2px}
  .services__list{list-style:none;font-size:6.8px;line-height:1.42}
  .contact__phone{position:absolute;left:24px;right:24px;top:322px;height:36px;border-left:1px solid var(--green);border-right:1px solid var(--green);text-align:center;padding-top:5px}
  .contact__label{font-size:6.5px;color:var(--muted);letter-spacing:.3px}
  .contact__number{font-family:"Fjalla One",Impact,sans-serif;font-size:10px;color:var(--green);margin-top:2px;letter-spacing:.5px}
  .contact__web{position:absolute;left:0;right:0;bottom:0;height:17px;background:var(--green-soft);font-size:6.5px;text-align:center;line-height:17px;color:var(--slate)}

  /* outside: cover panel */
  .cover{background:var(--slate)}
  .cover__visual{position:absolute;left:3px;right:3px;top:4px;height:184px;background:radial-gradient(circle at 75% 45%,#8fc24a 0,#3f6d3a 35%,#1d3a2a 70%),#244032}
  .cover__band{position:absolute;left:0;right:0;top:188px;height:96px;background:var(--green-soft);display:flex;align-items:center;justify-content:center}
  .cover__brand{font-size:30px}
  .cover__quote{position:absolute;left:0;right:0;top:318px;font-family:"Fjalla One",Impact,sans-serif;color:var(--paper);font-size:13px;line-height:1.15;text-align:center}

  /* inside: what panel */
  .what__shape{position:absolute;left:6px;top:6px}
  .what__title{position:absolute;left:14px;top:22px;font-family:"Fjalla One",Impact,sans-serif;color:var(--paper);font-size:22px;line-height:1.16;text-transform:uppercase;font-weight:400}
  .what__rule{position:absolute;left:14px;width:100px;height:1px;background:var(--paper)}
  .what__text{position:absolute;left:14px;right:10px;top:142px}

  /* inside: areas panel */
  .areas__title{font-size:20px;margin:14px 22px 0;line-height:1;padding:2px 0;border-top:2px solid var(--green);border-bottom:2px solid var(--green)}
  .areas__sub{font-size:7.3px;text-align:center;margin-top:6px}
  .areas__grid{display:grid;grid-template-columns:repeat(3,1fr);margin:8px 18px 0;row-gap:6px}
  .area{text-align:center;font-size:5.8px;font-weight:600}
  .area__dot{width:32px;height:32px;border-radius:50%;background:var(--green);margin:0 auto 4px}
  .areas__blob{position:absolute;left:80px;top:200px}
  .areas__text{position:relative;margin:8px 10px 0 12px}

  /* inside: how panel */
  .how__title{background:var(--slate);margin:8px 7px 0;padding:4px;font-size:11px}
  .how__blob{position:absolute;left:0;top:150px}
  .how__text{position:relative;margin:6px 7px 0 9px}
  .how__icon{float:left;width:30px;height:30px;border:2px solid var(--green);background:var(--slate);margin:2px 6px 2px 0}
  .how__icon--right{float:right;margin:2px 0 2px 6px}
</style>
</head>
<body>

<section class="spread spread--outside" aria-label="Brochure outside">
  <article class="panel expect">
    <h2 class="heading expect__title">What can I expect from regenerative medicine treatments</h2>
    <div class="body-copy">
      <p>During your visit, the team begins with a consultation and physical exam to determine if you're a candidate for regenerative medicine. They ask about your symptoms, condition, overall health, and lifestyle. If you're a candidate, the team then explains the procedure and what to expect both during and afterward.</p>
      <p>For the procedure, the team first cleans your skin and applies a topical numbing cream to your skin, if needed. Next, the team injects regenerative products into the treatment area. You may feel a slight pinch or burning sensation during the injection. The injection takes less than five minutes and you can return to your usual activities the same day. Mild soreness at the injection site is possible for two to three days.</p>
      <p>Over the coming weeks and months, the injected products help repair damaged tissues at the treatment site. Most people notice results after two months. Follow-up care may be recommended based on your condition and initial results. The team has seen dramatic results with regenerative medicine treatments, however, individual results can vary. Speak to the team to see if regenerative medicine is right for you.</p>
    </div>
  </article>

  <article class="panel contact">
    <div class="contact__top">
      <div class="event">
        <p class="event__title">Next Event / Class</p>
        <p class="event__row"><span class="event__label">Date</span><span class="event__line"></span></p>
        <p class="event__row"><span class="event__label">Time</span><span class="event__line"></span></p>
        <p class="event__row"><span class="event__label">Location</span><span class="event__line"></span></p>
        <p class="event__row"><span class="event__label"></span><span class="event__line"></span></p>
      </div>
    </div>
    <h2 class="heading contact__cta">To learn more, schedule a consultation online or by phone today</h2>
    <p class="brand-name contact__brand">CVR</p>
    <div class="services">
      <p class="services__title">Our Services</p>
      <ul class="services__list">
        <li>Stem cell allograft</li>
        <li>Platelet rich plasma (PRP)</li>
        <li>Prolotherapy</li>
        <li>Trigger point injection</li>
        <li>Chiropractic &amp; rehab therapies</li>
      </ul>
    </div>
    <div class="contact__phone">
      <p class="contact__label">CONTACT US</p>
      <p class="contact__number">555 010-2040</p>
    </div>
    <p class="contact__web">www.coastalvitalrestore.example</p>
  </article>

  <article class="panel cover">
    <div class="cover__visual" role="img" aria-label="Illustration of a glowing spine, shoulder, hand and knee joints highlighting pain areas"></div>
    <div class="cover__band"><p class="brand-name cover__brand">CVR</p></div>
    <p class="cover__quote">“ For Joint Arthritis,<br>Muscle Pain<br>&amp; Injuries ”</p>
  </article>
</section>

<section class="spread spread--inside" aria-label="Brochure inside">
  <article class="panel what">
    <svg class="what__shape" width="178" height="130" viewBox="0 0 178 130" aria-hidden="true">
      <path d="M0 0H178V40A95 95 0 0 1 20 126Q0 118 0 100Z" fill="#9bcb3c"/>
    </svg>
    <span class="what__rule" style="top:17px"></span>
    <h2 class="what__title">What is<br>regenerative<br>medicine</h2>
    <span class="what__rule" style="top:110px"></span>
    <div class="body-copy what__text">
      <p>Regenerative medicine is a form of biotechnology that involves injecting regenerative medicine products into injured tissues to help your body repair damage. Regenerative medicine uses tissue engineering techniques to repair muscles, ligaments, cartilage, and tendons damaged by injuries, overuse, and osteoarthritis. The medical providers at Coastal Vital Restore select from a variety of available treatments and products. These include amniotic allografts, hyaluronic acid, regenerative cells, and cytokines which are powerful growth factors that may help regenerate your own body's tissues.</p>
      <p>After you're injection with the amniotic allograft serum, the growth factors trigger repair at the site of injection. Over the course of the next several weeks, cells grow and multiply forming new tissue.</p>
    </div>
  </article>

  <article class="panel areas">
    <svg class="areas__blob" width="120" height="200" viewBox="0 0 120 200" aria-hidden="true">
      <circle cx="120" cy="130" r="118" fill="#cfe3a4"/>
    </svg>
    <h2 class="heading areas__title">Regenerative<br>medicine</h2>
    <p class="areas__sub">Used in the following areas</p>
    <div class="areas__grid">
      <div class="area"><div class="area__dot"></div>Shoulder</div>
      <div class="area"><div class="area__dot"></div>Wrist</div>
      <div class="area"><div class="area__dot"></div>Elbow</div>
      <div class="area"><div class="area__dot"></div>Hip</div>
      <div class="area"><div class="area__dot"></div>Ankle</div>
      <div class="area"><div class="area__dot"></div>Knee</div>
    </div>
    <div class="body-copy areas__text">
      <p>There are many additional types of bone and soft tissue problems, including arthritis, that these injections may benefit.</p>
      <p>With regenerative medicine and amniotic allograft treatments, the team supports the natural healing abilities of your body without the need for drugs or surgical repair and painful recovery.</p>
      <p>However, not all forms of regenerative medicine are equal. At Coastal Vital Restore, the team only works with the best regenerative medicine labs to ensure that the right kind of products are selected and that they are of the best quality and highest safety.</p>
    </div>
  </article>

  <article class="panel how">
    <svg class="how__blob" width="195" height="250" viewBox="0 0 195 250" aria-hidden="true">
      <path d="M0 30Q90 -10 195 20V250H0Z" fill="#cfe3a4"/>
    </svg>
    <h2 class="heading how__title">How does<br>regenerative medicine work</h2>
    <div class="body-copy how__text">
      <p><span class="how__icon"></span>The team uses lab-grade products that are sterilized and processed to inject into the injured area. Once injected, it is thought that these powerful products differentiate into a variety of tissues to trigger your own body to repair damaged tissues. This damage may involve minor tears in muscles, ligaments, and tendons, or cartilage and meniscus breakdown in joints.</p>
      <p><span class="how__icon how__icon--right"></span>Regenerative medicine products contain the basic building blocks of the body tissues — including proteins, amino acids, and cytokines — responsible for healing and tissue growth. They also provide anti-inflammatory benefits by promoting repair of tissues affected by inflammation.</p>
      <p><span class="how__icon"></span>While some inflammation is normal and has a benefit to healing injuries, long-term inflammation causes pain, swelling, and further damage to tissues. When you experience too much inflammation, it does more harm than good. Instead of constantly relying on anti-inflammatory medications, regenerative products may be able to correct the problem at the source and reduce the production of natural inflammatory chemicals so you can heal.</p>
    </div>
  </article>
</section>

</body>
</html>
```